GHollis Busisness Card

I am an aerospace consultant and at this time only need business cards.

Industry/Entity Type

Business

Contact Information for Business Card

Hollis Partners,LLC
Gerald T. Hollis

348 Birch Hollow Road
Madison AL 35762

256-555-0148 (cell)
256-555-0173 (fax)

geraldhollis@mailbrook.net

```html
<!DOCTYPE html>
<html lang="en">
<head>
<meta charset="utf-8">
<title>Hollis Partners, LLC — Business Card</title>
<link href="https://fonts.googleapis.com/css2?family=PT+Sans:wght@700&family=Open+Sans:wght@400;700&family=Arimo:wght@400&display=swap" rel="stylesheet">
<style>
  :root {
    --backdrop: #d9d9db;
    --card-dark: #58585a;
    --card-glow: #e8e8ea;
    --accent-blue: #0a87cf;
    --title-black: #0b0b0b;
    --text-white: #ffffff;
  }
  html, body {
    margin: 0;
    padding: 0;
    width: 1200px;
    height: 1200px;
    overflow: hidden;
    background: var(--backdrop);
  }
  .business-card {
    position: absolute;
    left: 60px;
    top: 293px;
    width: 1080px;
    height: 614px;
  }
  .business-card svg {
    display: block;
    width: 100%;
    height: 100%;
  }
  .company-name {
    font-family: "PT Sans", "Arial Narrow", sans-serif;
    font-weight: 700;
    font-size: 60px;
    fill: var(--title-black);
  }
  .person-name {
    font-family: "Open Sans", Verdana, sans-serif;
    font-weight: 700;
    font-size: 21px;
    fill: var(--accent-blue);
    letter-spacing: 0.5px;
  }
  .person-role {
    font-family: "Open Sans", Verdana, sans-serif;
    font-weight: 400;
    font-size: 17px;
    fill: var(--text-white);
  }
  .contact-line {
    font-family: "Arimo", Arial, sans-serif;
    font-size: 19px;
    fill: var(--text-white);
  }
  .contact-icon-disc { fill: var(--text-white); }
  .contact-icon-glyph { fill: var(--accent-blue); }
  .contact-icon-stroke { fill: none; stroke: var(--accent-blue); stroke-width: 1.4; }
</style>
</head>
<body>
  <div class="business-card">
    <svg viewBox="0 0 751 427" xmlns="http://www.w3.org/2000/svg">
      <defs>
        <radialGradient id="card-glow" cx="291" cy="135" r="300" gradientUnits="userSpaceOnUse" gradientTransform="translate(291 135) scale(1 1.05) translate(-291 -135)">
          <stop offset="0" stop-color="var(--card-glow)"/>
          <stop offset="0.45" stop-color="#a3a3a6"/>
          <stop offset="1" stop-color="var(--card-dark)"/>
        </radialGradient>
      </defs>

      <rect class="card-base" width="751" height="427" fill="var(--card-dark)"/>
      <rect class="card-glow" width="751" height="427" fill="url(#card-glow)"/>

      <path class="accent-swoosh" fill="var(--accent-blue)"
        d="M0,172 C150,203 370,220 560,182 C690,155 758,118 750,88 C742,58 640,18 470,0 L560,0
           C640,18 672,42 668,70 C662,115 520,168 340,188 C200,200 90,190 0,180 Z"/>

      <text class="company-name" x="41" y="110">Hollis Partners,LLC</text>

      <text class="person-name" x="95" y="280">Gerald T. Hollis</text>
      <text class="person-role" x="95" y="306">Aerospace consultant</text>

      <g class="contact-address">
        <circle class="contact-icon-disc" cx="407" cy="274" r="8"/>
        <path class="contact-icon-glyph" d="M401,274 L407,268.5 L413,274 L411.5,274 L411.5,279 L402.5,279 L402.5,274 Z"/>
        <text class="contact-line" x="429" y="281">348 Birch Hollow Road Madison</text>
        <text class="contact-line" x="429" y="307">AL 35762</text>
      </g>

      <g class="contact-phone">
        <circle class="contact-icon-disc" cx="407" cy="332" r="8"/>
        <path class="contact-icon-glyph" d="M402.5,336 C404,330 406,328 411,326.5 L412,329 L409.5,330.5 C408.5,331.5 407.5,333 407,334.5 L405,337.5 Z"/>
        <text class="contact-line" x="429" y="339">256-555-0148</text>
      </g>

      <g class="contact-fax">
        <circle class="contact-icon-disc" cx="407" cy="360" r="8"/>
        <rect class="contact-icon-glyph" x="402" y="358" width="10" height="6" rx="1"/>
        <rect class="contact-icon-stroke" x="404.5" y="354.5" width="5" height="4"/>
        <text class="contact-line" x="429" y="367">256-555-0173</text>
      </g>

      <g class="contact-email">
        <circle class="contact-icon-disc" cx="407" cy="388" r="8"/>
        <rect class="contact-icon-glyph" x="401.5" y="384" width="11" height="8" rx="0.8"/>
        <path d="M402,384.5 L407,388.8 L412,384.5" fill="none" stroke="var(--text-white)" stroke-width="1.1"/>
        <text class="contact-line" x="429" y="395">geraldhollis@mailbrook.net</text>
      </g>
    </svg>
  </div>
</body>
</html>
```